Bright Fern Painting needs a new business card. See attachments for our logo and current card as an example.
We want to utilize the same colors in the logo, and keep all the information that is currently on it. Just need an updated and modern design.
We are open to loosing the Association Logos if it means a better design.
We are also entertaining a spot for a picture of a headshot of the person listed on the card. Head shot can be finished later.

```html
<!DOCTYPE html>
<html lang="en">
<head>
<meta charset="utf-8">
<title>Bright Fern Painting – Business Card</title>
<link href="https://fonts.googleapis.com/css2?family=Source+Sans+3:wght@400;600;700&display=swap" rel="stylesheet">
<style>
  :root{
    --fern:#414d34;
    --fern-dark:#343e2a;
    --maroon:#6b3530;
    --paper:#ffffff;
    --ink-light:#f3f1ec;
    --stage:#e6e6e3;
    --photo-a:#6f8683;
    --photo-b:#3d4f50;
  }
  *{box-sizing:border-box;margin:0;padding:0}
  html,body{width:1200px;height:900px;overflow:hidden}
  body{background:var(--stage);font-family:"Source Sans 3",sans-serif;position:relative}

  .card{position:absolute;border-radius:22px;overflow:hidden;box-shadow:0 10px 30px rgba(0,0,0,.18)}

  /* Back: person card */
  .card--person{left:90px;top:152px;width:340px;height:595px;background:var(--fern)}
  .person__art{position:absolute;left:0;top:0;width:340px;height:340px}
  .person__info{position:absolute;left:0;right:0;top:350px;text-align:center;color:var(--ink-light)}
  .person__name{font-weight:700;font-size:27px;letter-spacing:1px;text-transform:uppercase}
  .person__role{font-size:19px;margin-top:2px;letter-spacing:.5px}
  .contact-divider{display:flex;align-items:center;justify-content:center;gap:8px;margin:22px 0 20px}
  .contact-divider__rule{width:44px;height:1.5px;background:var(--ink-light)}
  .contact-icon{width:34px;height:34px;border-radius:50%;background:var(--paper);display:flex;align-items:center;justify-content:center}
  .contact-icon svg{width:19px;height:19px}
  .contact-list{list-style:none;font-size:19px;line-height:1.45;letter-spacing:.3px}

  /* Front: company card */
  .card--company{left:480px;top:273px;width:630px;height:360px;background:var(--paper)}
  .brand{position:absolute;left:0;right:0;top:70px;display:flex;align-items:center;justify-content:center;gap:18px}
  .brand__mark{width:26px;height:26px;background:var(--maroon)}
  .brand__name{font-weight:700;font-size:46px;line-height:1.05;color:var(--fern);text-transform:uppercase;letter-spacing:1px}
  .services{position:absolute;left:0;right:0;bottom:0;height:92px;background:var(--fern);display:flex;align-items:center;justify-content:space-around;padding:0 26px;list-style:none}
  .service{display:flex;align-items:center;gap:8px;color:var(--ink-light);font-size:21px;font-weight:600}
  .service__box{width:22px;height:22px}
</style>
</head>
<body>

<section class="card card--person">
  <svg class="person__art" viewBox="0 0 340 340" xmlns="http://www.w3.org/2000/svg">
    <defs>
      <linearGradient id="photoTone" x1="0" y1="0" x2="1" y2="1">
        <stop offset="0" stop-color="var(--photo-a)"/>
        <stop offset="1" stop-color="var(--photo-b)"/>
      </linearGradient>
    </defs>
    <path role="img" aria-label="Headshot photo of Daniel Harper" d="M0 0 H300 C300 150 215 270 0 300 Z" fill="url(#photoTone)"/>
    <path d="M0 300 C215 270 300 150 300 0 H318 C318 175 232 305 0 332 Z" fill="var(--maroon)"/>
    <path d="M0 338 C240 312 330 180 330 0" fill="none" stroke="var(--paper)" stroke-width="3"/>
  </svg>

  <div class="person__info">
    <h1 class="person__name">Daniel Harper</h1>
    <p class="person__role">Quality Manager</p>
    <div class="contact-divider">
      <span class="contact-divider__rule"></span>
      <span class="contact-icon"><svg viewBox="0 0 24 24"><path fill="var(--maroon)" d="M6.6 10.8a15 15 0 0 0 6.6 6.6l2.2-2.2c.3-.3.7-.4 1-.2 1.1.4 2.3.6 3.6.6.6 0 1 .4 1 1V20c0 .6-.4 1-1 1A17 17 0 0 1 3 4c0-.6.4-1 1-1h3.5c.6 0 1 .4 1 1 0 1.3.2 2.5.6 3.6.1.3 0 .7-.2 1z"/></svg></span>
      <span class="contact-icon"><svg viewBox="0 0 24 24"><rect x="2" y="5" width="20" height="14" rx="1" fill="var(--maroon)"/><path d="M2.5 5.5 12 13l9.5-7.5" fill="none" stroke="#fff" stroke-width="1.5"/></svg></span>
      <span class="contact-icon"><svg viewBox="0 0 24 24" fill="none" stroke="var(--maroon)" stroke-width="1.6"><circle cx="12" cy="12" r="9"/><ellipse cx="12" cy="12" rx="4" ry="9"/><path d="M3 12h18M4.5 7.5h15M4.5 16.5h15"/></svg></span>
      <span class="contact-divider__rule"></span>
    </div>
    <ul class="contact-list">
      <li>262-555-0148</li>
      <li>Daniel.BrightFern@mail.com</li>
      <li>BrightFernPainting.com</li>
    </ul>
  </div>
</section>

<section class="card card--company">
  <div class="brand">
    <span class="brand__mark"></span>
    <p class="brand__name">Bright Fern<br>Painting</p>
  </div>
  <ul class="services">
    <li class="service"><svg class="service__box" viewBox="0 0 22 22"><rect x="1" y="1" width="20" height="20" fill="none" stroke="#f3f1ec" stroke-width="1.8"/><path d="M5 11l4 4 8-9" fill="none" stroke="#f3f1ec" stroke-width="2.2"/></svg>Interior</li>
    <li class="service"><svg class="service__box" viewBox="0 0 22 22"><rect x="1" y="1" width="20" height="20" fill="none" stroke="#f3f1ec" stroke-width="1.8"/><path d="M5 11l4 4 8-9" fill="none" stroke="#f3f1ec" stroke-width="2.2"/></svg>Exterior</li>
    <li class="service"><svg class="service__box" viewBox="0 0 22 22"><rect x="1" y="1" width="20" height="20" fill="none" stroke="#f3f1ec" stroke-width="1.8"/><path d="M5 11l4 4 8-9" fill="none" stroke="#f3f1ec" stroke-width="2.2"/></svg>Carpentry</li>
    <li class="service"><svg class="service__box" viewBox="0 0 22 22"><rect x="1" y="1" width="20" height="20" fill="none" stroke="#f3f1ec" stroke-width="1.8"/><path d="M5 11l4 4 8-9" fill="none" stroke="#f3f1ec" stroke-width="2.2"/></svg>Drywall</li>
  </ul>
</section>

</body>
</html>
```